Under The Lanterns a Tola Rin Project - Not for profit project

I am looking for a basic template to use on webnode.
The site is for a charitable organization aimed at adults and importantly children. I have attached the copy. The theme of Tola Rin ( Tola Meadow in Spanish) is our family initials and the idea is to make it fun or at least interesting. We will translate the site to Spanish also. The power of waves and the power of a Greek god like Poseidon could be a good fit in developing the idea of creating waves of positive change. BUT the Wave theme and Poseidon need to be bright colours fun and inspiring. I dont want the site to look like a fantasy novel cover. Or a display of some amazing mans body as that is not the fit. Poseidon could be illustrated version. The Wave man drawing is something my daughter did and is fun and could work to engage , who will ultimately be the one to drive this project forward. But the “Wave Man” is not mandatory.
I would prefer if the colors are not dark or depressing. In fact this is one of the reasons I am looking for a designer - so that the designer can find a way to present the wave theme but in a bright, uplifting tone.

I will use webnode templates so I am guessing the design would be in the form of background graphics that can be used on the webnode platform. But I need your suggestions on this ?

Target Market(s)

Anyone interested in creating a fairer world

Industry/Entity Type

Democracy

Number of Pages Required

3 page

Requirements
Must have
• Basic template -
Nice to have
• None are essential but ; Waves, Wave man, Poisedon or other greek gods

```html
<!DOCTYPE html>
<html lang="en">
<head>
<meta charset="utf-8">
<title>Under The Lanterns — A Tola Rin Fund</title>
<link href="https://fonts.googleapis.com/css2?family=Manrope:wght@400;500;700;800&family=Playfair+Display:wght@700;800&display=swap" rel="stylesheet">
<style>
  :root {
    --sky: #5b8ec6;
    --sea-deep: #1f6f95;
    --sea-teal: #2f92ae;
    --foam: #e9f3f8;
    --page: #e6f4fb;
    --brand-blue: #1599d0;
    --pill: #139ee0;
    --ink: #1d2a33;
    --white: #ffffff;
    --band-light: #d7ecf2;
    --band-dark: #0b1a24;
    --figure-tint: #cde9f6;
  }
  * { margin: 0; padding: 0; box-sizing: border-box; }
  html, body { width: 1090px; height: 1200px; overflow: hidden; }
  body { background: var(--page); font-family: "Manrope", sans-serif; color: var(--ink); position: relative; }

  .hero {
    position: absolute; left: 0; top: 0; width: 1090px; height: 660px;
    background:
      radial-gradient(ellipse 320px 300px at 120px 330px, rgba(240,247,250,0.95), rgba(240,247,250,0) 70%),
      radial-gradient(ellipse 260px 200px at 330px 420px, rgba(200,232,240,0.8), rgba(200,232,240,0) 70%),
      radial-gradient(ellipse 420px 260px at 760px 280px, rgba(40,130,160,0.9), rgba(40,130,160,0) 75%),
      linear-gradient(180deg, var(--sky) 0%, #4f8fb8 25%, var(--sea-teal) 50%, var(--sea-deep) 80%, #3d7fa6 100%);
  }
  .hero-photo { position: absolute; inset: 0; }

  .site-header { position: absolute; left: 0; top: 0; width: 100%; height: 86px; }
  .logo {
    position: absolute; left: 120px; top: 24px;
    font-family: "Playfair Display", serif; font-weight: 800; font-size: 28px; color: var(--white);
  }
  .main-nav { position: absolute; left: 504px; top: 28px; display: flex; align-items: center; }
  .main-nav a {
    color: var(--white); text-decoration: none; font-size: 14.5px; font-weight: 500;
    height: 32px; line-height: 32px; padding: 0 14px; margin-right: 3px; border-radius: 16px;
  }
  .main-nav a.active { background: var(--pill); }

  .hero-content { position: absolute; left: 0; top: 180px; width: 100%; text-align: center; color: var(--white); }
  .play-icon { display: block; margin: 0 auto; }
  .hero-title { font-weight: 800; font-size: 46px; letter-spacing: -0.5px; margin-top: 24px; line-height: 1; }
  .hero-text { font-size: 17px; line-height: 26px; margin: 28px auto 0; width: 560px; font-weight: 500; }
  .read-more {
    display: inline-block; margin-top: 26px; background: var(--white); color: var(--brand-blue);
    font-weight: 700; font-size: 14.5px; width: 124px; height: 41px; line-height: 41px; border-radius: 12px;
    text-decoration: none;
  }

  .wave-divider { position: absolute; left: 0; top: 510px; }

  .site-footer { position: absolute; left: 0; top: 660px; width: 100%; text-align: center; }
  .footer-title {
    font-family: "Playfair Display", serif; font-weight: 800; font-size: 35px; color: var(--brand-blue);
    margin-top: 18px;
  }
  .address-row { display: flex; align-items: center; justify-content: center; margin-top: 30px; }
  .address-row .rule { width: 161px; height: 1.5px; background: var(--brand-blue); }
  .address-row span { font-size: 14px; letter-spacing: 1.2px; padding: 0 14px; }
  .footer-nav { display: flex; justify-content: center; margin-top: 28px; }
  .footer-nav a { color: var(--ink); text-decoration: none; font-size: 14px; margin: 0 15px; }
  .footer-rule { width: 573px; height: 1.5px; background: var(--brand-blue); margin: 28px 0 0 261px; }
  .follow-row { display: flex; align-items: center; justify-content: center; margin-top: 36px; }
  .follow-row .label { font-size: 14px; letter-spacing: 1.2px; margin-right: 20px; }
  .social-dot { width: 28px; height: 28px; border-radius: 50%; border: 1.5px solid var(--brand-blue); margin: 0 3px; }
  .copyright { font-size: 11px; margin-top: 30px; }

  .figures-band {
    position: absolute; left: 0; top: 1000px; width: 1090px; height: 200px;
    background: linear-gradient(180deg, rgba(205,233,246,0) 0%, var(--figure-tint) 60%, var(--figure-tint) 100%);
  }
</style>
</head>
<body>
  <section class="hero">
    <div class="hero-photo" role="img" aria-label="Photograph of a large blue ocean wave breaking with white spray"></div>

    <header class="site-header">
      <div class="logo">Under The Lanterns</div>
      <nav class="main-nav">
        <a class="active" href="#">HOME</a>
        <a href="#">MISSION</a>
        <a href="#">WHO</a>
        <a href="#">FOCUS</a>
        <a href="#">BLOG</a>
        <a href="#">CONTACT</a>
      </nav>
    </header>

    <div class="hero-content">
      <svg class="play-icon" width="48" height="48" viewBox="0 0 48 48" aria-hidden="true">
        <circle cx="24" cy="24" r="21.5" fill="none" stroke="#fff" stroke-width="3"/>
        <path d="M19 15 L33 24 L19 33 Z" fill="#fff"/>
      </svg>
      <h1 class="hero-title">A TOLA RIN FUND</h1>
      <p class="hero-text">Never doubt that a small group of committed citizens can change the world. Indeed, it's the only thing that ever has</p>
      <a class="read-more" href="#">READ MORE</a>
    </div>
  </section>

  <svg class="wave-divider" width="1090" height="150" viewBox="0 0 1090 150" aria-hidden="true">
    <path d="M0,60 C260,90 520,30 780,22 C900,18 1000,26 1090,42 L1090,150 L0,150 Z" fill="var(--band-light)" opacity="0.8"/>
    <path d="M0,75 C260,105 520,45 780,36 C900,32 1000,40 1090,58 L1090,75 C1000,58 900,52 780,55 C520,65 260,120 0,95 Z" fill="var(--band-dark)"/>
    <path d="M0,95 C260,120 520,65 780,55 C900,52 1000,58 1090,75 L1090,150 L0,150 Z" fill="var(--band-light)"/>
    <path d="M0,108 C260,132 520,82 780,72 C900,69 1000,76 1090,92 L1090,150 L0,150 Z" fill="var(--band-dark)" opacity="0.85"/>
    <path d="M0,122 C260,146 520,98 780,88 C900,85 1000,92 1090,108 L1090,150 L0,150 Z" fill="var(--page)"/>
  </svg>

  <footer class="site-footer">
    <h2 class="footer-title">Under The Lanterns</h2>
    <div class="address-row">
      <div class="rule"></div>
      <span>48 Harbor Lane, Port Evlin, NE 20417</span>
      <div class="rule"></div>
    </div>
    <nav class="footer-nav">
      <a href="#">Home</a>
      <a href="#">Mission</a>
      <a href="#">Who</a>
      <a href="#">Focus</a>
      <a href="#">Blog</a>
      <a href="#">Contact</a>
    </nav>
    <div class="footer-rule"></div>
    <div class="follow-row">
      <span class="label">Follow us</span>
      <div class="social-dot"></div>
      <div class="social-dot"></div>
      <div class="social-dot"></div>
      <div class="social-dot"></div>
      <div class="social-dot"></div>
    </div>
    <p class="copyright">Copyright © 2024 All Rights Reserved</p>
  </footer>

  <div class="figures-band" role="img" aria-label="Faint light-blue silhouettes of Greek warriors, archers and a rearing horse"></div>
</body>
</html>
```